We are looking to recreate our Harlow & Partners Jobsite Sign. This sign will be placed by the street at each of our jobsites. We want to keep this sign simple, but at the same time, want to add a catching appeal to the design for anyone passing by. We want to stick to a two color scheme (Harlow Blue, and White). Please only use the Company Logo that I have uploaded for this project. Please also see a mock up of what we would like to include on this sign. The Sign Dimensions will be 4' x 8'. Please keep all verbiage uniform with the verbiage on the sample design I have uploaded. LET YOUR CREATIVITY FLOW!

```html
<!DOCTYPE html>
<html lang="en">
<head>
<meta charset="utf-8">
<title>Harlow &amp; Partners Jobsite Sign</title>
<link href="https://fonts.googleapis.com/css2?family=Noto+Serif:wght@700&display=swap" rel="stylesheet">
<style>
  :root {
    --harlow-blue: #27318f;
    --sign-white: #ffffff;
    --backdrop: #8dc3f2;
  }
  * { margin: 0; padding: 0; box-sizing: border-box; }
  html, body {
    width: 1109px; height: 1200px; overflow: hidden;
    background: var(--backdrop);
  }
  body { position: relative; font-family: "Noto Serif", Georgia, serif; font-weight: 700; }
  .jobsite-sign {
    position: absolute; left: 54px; top: 350px;
    width: 1000px; height: 500px;
    background: var(--sign-white);
    box-shadow: 0 2px 6px rgba(0,0,0,0.25);
    color: var(--harlow-blue);
  }
  .top-rule {
    position: absolute; left: 15px; right: 15px; top: 13px; height: 16px;
    background: var(--harlow-blue);
  }
  .brand-row {
    position: absolute; left: 15px; right: 15px; top: 45px; height: 125px;
  }
  .company-name {
    position: absolute; right: 508px; top: 10px; text-align: right; line-height: 1;
    color: var(--harlow-blue);
  }
  .company-name .name-main { display: block; font-size: 68px; letter-spacing: -1px; }
  .company-name .name-sub { display: block; font-size: 30px; margin-top: 2px; }
  .brand-divider {
    position: absolute; left: 479px; top: 5px; width: 3px; height: 115px;
    background: var(--harlow-blue);
  }
  .trade-title {
    position: absolute; left: 500px; top: 12px; text-align: center;
    font-size: 50px; line-height: 1.0;
  }
  .info-panel {
    position: absolute; left: 15px; right: 15px; top: 187px; height: 207px;
    background: var(--harlow-blue);
    color: var(--sign-white); text-align: center;
  }
  .tagline { font-size: 49px; margin-top: 18px; line-height: 1.1; }
  .licence-line { font-size: 29px; margin-top: 6px; line-height: 1.1; letter-spacing: 0.5px; }
  .web-address { font-size: 48px; margin-top: 6px; letter-spacing: 2px; line-height: 1.2; }
  .contact-row { position: absolute; left: 15px; right: 15px; top: 394px; height: 92px; }
  .contact-wedge { position: absolute; left: 0; top: 0; width: 970px; height: 92px; }
  .phone-line {
    position: absolute; left: 28px; top: 6px; font-size: 66px; line-height: 1.2;
    color: var(--harlow-blue); letter-spacing: 1px;
  }
</style>
</head>
<body>
  <main class="jobsite-sign">
    <div class="top-rule"></div>
    <header class="brand-row">
      <div class="company-name">
        <span class="name-main">Harlow</span>
        <span class="name-sub">&amp; Partners, Inc.</span>
      </div>
      <div class="brand-divider"></div>
      <div class="trade-title">General<br>Contractors</div>
    </header>
    <section class="info-panel">
      <p class="tagline">“We Build Lasting Confidence”</p>
      <p class="licence-line">Lakemont, Florida - CGC4821937</p>
      <p class="web-address">harlowpartners.net</p>
    </section>
    <footer class="contact-row">
      <svg class="contact-wedge" viewBox="0 0 970 92">
        <polygon points="652,0 970,0 970,92 715,92" fill="var(--harlow-blue)"/>
        <g fill="var(--sign-white)">
          <circle cx="757" cy="43" r="25" role="img" aria-label="Social profile link"/>
          <circle cx="846" cy="43" r="25" role="img" aria-label="Social profile link"/>
          <circle cx="934" cy="43" r="25" role="img" aria-label="Social profile link"/>
        </g>
      </svg>
      <p class="phone-line">Call: 555-214-0387</p>
    </footer>
  </main>
</body>
</html>
```